Flat bootstrap design for existing site

I'm looking for a modern flat design based around an existing logo. This has to be a custom design (no external templates), and implemented into a bootstrap framework.

The logo is attached as 2 versions - choose whichever you want, that flows better with whatever design you choose.

Added screenshots of the existing site (currently using the default bootstrap layouts). Please make your designs around those pages in the screenshots (i.e. the homepage only has the postal code input and the header). The active page has 3 screenshots, because I wanted to illustrate the other states that would be visible (in the table rows).

This is a moving/junk removal website, just for some context.

Here's some example websites (flat designs) that I like, just to give you an idea of what I'm after.

https://www.plivento.com/
https://hoskadel.com/
https://trumvex.com/
https://bravolinth.com/en/

• It must be a modern/simple flat design, that is built around the existing logo (attached).
• It has to be implemented using bootstrap.

```html
<!DOCTYPE html>
<html lang="en">
<head>
<meta charset="utf-8">
<title>Trovalo — Junk Removal &amp; Moving</title>
<link href="https://fonts.googleapis.com/css2?family=Roboto:wght@300;400;500;700&family=Roboto+Condensed:wght@400;700&family=Roboto+Slab:wght@300;400&display=swap" rel="stylesheet">
<style>
:root{
  --sky:#4cc6f2;
  --blue:#1b9fd8;
  --band:#4fb5df;
  --deep:#1a8cc4;
  --navy:#3b4560;
  --ink:#444;
  --muted:#777;
  --line:#d5dbe2;
  --light:#f2f2f2;
  --white:#fff;
  --star:#f5a623;
}
*{box-sizing:border-box;margin:0;padding:0}
html,body{width:1200px;height:2719px;overflow:hidden}
body{position:relative;font-family:"Roboto",Arial,sans-serif;color:var(--ink);background:var(--white)}
.abs{position:absolute}
/* top bar */
.topbar{left:0;top:0;width:1200px;height:33px;background:var(--white)}
.topbar .tagline{left:160px;top:9px;font-size:13px;color:#333}
.topbar .social{top:11px;width:11px;height:11px;border-radius:50%;background:#555}
.search{left:852px;top:3px;width:187px;height:27px;border:1px solid #e3e3e3;display:flex}
.search span{flex:1;font-size:10px;color:#888;padding:7px 8px}
.search b{width:35px;border-left:1px solid #e3e3e3;display:flex;align-items:center;justify-content:center}
/* nav */
.nav{left:0;top:33px;width:1200px;height:79px;background:var(--sky)}
.brand{left:160px;top:22px;font-size:32px;font-weight:500;color:var(--white);letter-spacing:1px}
.nav a{position:absolute;top:31px;color:var(--white);font-size:15px;text-decoration:none}
/* hero */
.hero{left:0;top:112px;width:1200px;height:481px;background:linear-gradient(90deg,#3d5678 0%,#4c6788 40%,#6b5a4f 55%,#8a5c44 75%,#4b4845 100%)}
.hero h1{position:absolute;left:160px;top:152px;font-family:"Roboto Condensed",sans-serif;font-weight:700;font-size:46px;line-height:46px;color:var(--white);text-transform:uppercase}
.postal{left:160px;top:280px;width:228px;height:39px;background:var(--white);font-size:12px;color:#333;padding:12px 11px}
.book-btn{left:388px;top:280px;width:116px;height:39px;background:var(--sky);color:var(--white);font-family:"Roboto Condensed",sans-serif;font-size:17px;font-weight:700;display:flex;align-items:center;justify-content:center;gap:5px}
/* steps */
.easy{left:0;top:593px;width:1200px;height:177px;background:linear-gradient(180deg,#fafafa,#eeeeee)}
.section-title{position:absolute;width:100%;text-align:center}
.easy h2{top:30px;font-family:"Roboto Slab",serif;font-weight:300;font-size:31px;color:#444;text-transform:uppercase}
.divider{height:2px;background:var(--deep)}
.divider::before,.divider::after{content:"";position:absolute;top:-3px;width:8px;height:8px;border-radius:50%;background:var(--deep)}
.divider::before{left:-4px}.divider::after{right:-4px}
.steps-band{left:0;top:770px;width:1200px;height:305px;background:var(--band);border-top:3px solid var(--deep)}
.step{top:716px;width:269px;height:196px;background:var(--blue);border:1px solid #7fd0f0;color:var(--white);text-align:center}
.step svg{margin-top:34px}
.step h3{font-family:"Roboto Slab",serif;font-weight:400;font-size:24px;margin-top:2px}
.step p{font-size:10.5px;line-height:14px;padding:0 22px;margin-top:6px}
.call{left:0;top:950px;width:1200px;text-align:center;color:var(--white);font-size:31px;display:flex;justify-content:center;align-items:center;gap:12px}
.call i{width:37px;height:37px;border:2px solid var(--white);border-radius:50%;display:flex;align-items:center;justify-content:center}
/* welcome */
.welcome h2{position:absolute;left:160px;top:1108px;font-family:"Roboto Condensed",sans-serif;font-weight:700;font-size:36px;color:var(--blue)}
.welcome p{position:absolute;left:160px;width:480px;font-size:11px;line-height:17px;color:#555}
.quote-head{left:696px;top:1022px;width:343px;height:53px;background:var(--navy);color:var(--white);font-size:21px;text-align:center;line-height:53px}
.quote-box{left:696px;top:1075px;width:343px;height:363px;border:1px solid #c7d3de;border-top:none;background:#fafbfc}
.field{left:720px;width:295px;border:1px solid var(--line);background:var(--white);font-size:10px;color:#333;display:flex;align-items:center;gap:8px;padding:0 12px}
.send{left:796px;top:1390px;width:143px;height:32px;background:var(--sky);border-radius:3px;color:var(--white);font-size:15px;display:flex;align-items:center;justify-content:center;gap:6px}
/* services */
.svc-rule{left:0;top:1481px;width:1200px;height:3px;background:var(--deep)}
.svc-photo{left:0;top:1487px;width:598px;height:531px;background:linear-gradient(180deg,#a9b3bb 0%,#c9c6bd 45%,#8f7b62 75%,#5e5246 100%)}
.svc-list{left:598px;top:1487px;width:602px;height:531px;background:var(--light)}
.svc{left:625px;width:415px;height:90px;border-bottom:1px solid #dcdcdc}
.svc .ic{position:absolute;left:0;top:0;width:55px;height:55px;border:2px solid #555;border-radius:50%;background:var(--white);display:flex;align-items:center;justify-content:center}
.svc h4{position:absolute;left:68px;top:0;font-family:"Roboto Condensed",sans-serif;font-weight:400;font-size:23px;color:var(--blue);text-transform:uppercase}
.svc p{position:absolute;left:68px;top:32px;width:340px;font-size:11px;line-height:15px;color:#555}
/* plan */
.plan{left:0;top:2018px;width:1200px;height:192px;background:var(--band);text-align:center;color:var(--white)}
.plan h2{margin-top:34px;font-family:"Roboto Condensed",sans-serif;font-weight:700;font-size:36px;text-transform:uppercase}
.plan p{width:600px;margin:6px auto 0;font-size:11px;line-height:17px}
.plan-btn{left:528px;top:134px;width:143px;height:33px;border:1px solid var(--white);border-radius:3px;background:#5fc3ea;font-size:16px;display:flex;align-items:center;justify-content:center;gap:6px}
/* testimonials */
.testi h2{top:2240px;font-family:"Roboto Condensed",sans-serif;font-weight:700;font-size:33px;color:var(--blue)}
.testi .sub{top:2280px;font-size:11px;color:#888}
.card{top:2359px;width:431px;height:177px;border:1px solid #7fc3e6;background:var(--white)}
.avatar{position:absolute;left:14px;top:20px;width:124px;height:124px;border-radius:50%;border:2px solid #9cd1ee;padding:6px}
.avatar div{width:100%;height:100%;border-radius:50%}
.card h5{position:absolute;left:152px;top:20px;font-size:15px;font-weight:500;color:#222}
.card .role{position:absolute;left:152px;top:60px;font-size:9.5px;font-weight:700;color:#222}
.card p{position:absolute;left:152px;top:97px;width:260px;font-size:10.5px;line-height:15px;color:#333}
.card .rating{position:absolute;left:152px;top:147px;font-size:11px;color:var(--star)}
.card .rating span{font-size:9.5px;margin-left:6px}
.pager{top:2573px;width:13px;height:13px;background:#ddd}
/* footer */
.footer{left:0;top:2623px;width:1200px;height:96px;background:var(--deep);text-align:center;color:var(--white)}
.footer .dots{display:flex;justify-content:center;gap:8px;margin-top:25px}
.footer .dots i{width:25px;height:25px;border-radius:50%;background:var(--white)}
.footer small{display:block;margin-top:12px;font-size:11px;letter-spacing:.5px}
</style>
</head>
<body>

<header>
  <div class="abs topbar">
    <span class="abs tagline">Deliver around the world!</span>
    <i class="abs social" style="left:780px"></i>
    <i class="abs social" style="left:801px"></i>
    <i class="abs social" style="left:822px"></i>
    <div class="abs search"><span>Search Keyword</span><b><svg width="11" height="11" viewBox="0 0 12 12"><circle cx="5" cy="5" r="3.6" fill="none" stroke="#333" stroke-width="1.5"/><path d="M7.7 7.7 11 11" stroke="#333" stroke-width="1.6"/></svg></b></div>
  </div>
  <nav class="abs nav">
    <span class="abs brand">Trovalo</span>
    <a style="left:493px">Book</a>
    <a style="left:628px">How it works</a>
    <a style="left:805px">Become a Driver</a>
    <a style="left:994px">Sign in</a>
  </nav>
</header>

<section class="abs hero" role="img" aria-label="Photo of a mover in a safety vest loading a truck">
  <h1>Need junk removed?<br>Book now.</h1>
  <div class="abs postal">Postal code</div>
  <div class="abs book-btn"><svg width="13" height="13" viewBox="0 0 14 14"><circle cx="7" cy="7" r="6" fill="none" stroke="#fff" stroke-width="1.6"/><path d="M5.5 4 8.5 7 5.5 10" fill="none" stroke="#fff" stroke-width="1.6"/></svg>Book Now!</div>
</section>

<section class="abs easy">
  <h2 class="section-title">Moving never can't be more easy!</h2>
  <div class="abs divider" style="left:293px;top:82px;width:620px"></div>
</section>
<div class="abs steps-band"></div>

<article class="abs step" style="left:161px">
  <svg width="92" height="62" viewBox="0 0 92 62" fill="none" stroke="#fff" stroke-width="2"><rect x="38" y="16" width="40" height="26" rx="2" transform="rotate(-35 58 29)"/><path d="M20 56h60"/><circle cx="22" cy="14" r="8"/><path d="M10 56V36q0-10 12-10t14 14"/></svg>
  <h3>Preapring</h3>
  <p>Lorem Ipsum is simply dummy text of the printing and typesetting industry. Lorem Ipsum has been the industry's standard dummy text...</p>
</article>
<article class="abs step" style="left:466px">
  <svg width="60" height="62" viewBox="0 0 60 62" fill="none" stroke="#fff" stroke-width="2"><rect x="22" y="2" width="18" height="14"/><rect x="20" y="16" width="22" height="16"/><circle cx="16" cy="24" r="5"/><path d="M12 60V34h8v26M20 38h4"/></svg>
  <h3>Collecting</h3>
  <p>Lorem Ipsum is simply dummy text of the printing and typesetting industry. Lorem Ipsum has been the industry's standard dummy text...</p>
</article>
<article class="abs step" style="left:770px">
  <svg width="70" height="62" viewBox="0 0 70 62" fill="none" stroke="#fff" stroke-width="2"><rect x="4" y="12" width="40" height="32" rx="2"/><path d="M44 22h12l10 12v10H44z"/><circle cx="16" cy="48" r="6"/><circle cx="54" cy="48" r="6"/><path d="M10 20h26M10 28h26"/></svg>
  <h3>Loading</h3>
  <p>Lorem Ipsum is simply dummy text of the printing and typesetting industry. Lorem Ipsum has been the industry's standard dummy text...</p>
</article>

<div class="abs call"><i><svg width="16" height="18" viewBox="0 0 16 18"><rect x="3" y="1" width="10" height="16" rx="2" fill="none" stroke="#fff" stroke-width="1.6"/><path d="M6 5h4M6 8h4M6 11h4" stroke="#fff" stroke-width="1.4"/></svg></i>Call Us: 000-000-0000</div>

<section class="welcome">
  <h2>WELCOME!</h2>
  <div class="abs divider" style="left:164px;top:1159px;width:403px"></div>
  <p style="top:1184px">Lorem Ipsum is simply dummy text of the printing and typesetting industry. Lorem Ipsum has been the industry's standard dummy text ever since the 1500s, when an unknown printer took a galley of type and scrambled it to make a type specimen book. It has survived not only five centuries, but also the leap into electronic typesetting, remaining essentially unchanged. It was popularised in the 1960s with the release of Letraset sheets containing Lorem Ipsum passages, and more recently with desktop publishing software like Aldus PageMaker including versions of Lorem Ipsum.</p>
  <p style="top:1315px">Lorem Ipsum is simply dummy text of the printing and typesetting industry. Lorem Ipsum has been the industry's standard dummy text ever since the 1500s, when an unknown printer took a galley of type and scrambled it to make a type specimen book. It has survived not only five centuries, but also the leap into electronic typesetting...</p>
</section>

<aside>
  <div class="abs quote-head">GET A QUOTE!</div>
  <div class="abs quote-box"></div>
  <div class="abs field" style="top:1097px;height:36px"><svg width="12" height="12" viewBox="0 0 12 12" fill="none" stroke="#555"><circle cx="6" cy="4" r="2.6"/><path d="M1.5 11.5q0-4.5 4.5-4.5t4.5 4.5z"/></svg>Name</div>
  <div class="abs field" style="top:1148px;height:36px"><svg width="12" height="12" viewBox="0 0 12 12" fill="none" stroke="#555"><path d="M2 1.5h2.5l1 3-1.5 1q1 2 3 3l1-1.5 3 1V10q0 1.5-1.5 1.5Q1 11 .5 3 .5 1.5 2 1.5z"/></svg>Phone</div>
  <div class="abs field" style="top:1201px;height:37px"><svg width="13" height="10" viewBox="0 0 13 10" fill="none" stroke="#555"><rect x=".5" y=".5" width="12" height="9"/><path d="m.5 .5 6 5 6-5"/></svg>Email</div>
  <div class="abs field" style="top:1255px;height:117px;align-items:flex-start;padding-top:11px">Description</div>
  <div class="abs send"><svg width="12" height="12" viewBox="0 0 14 14"><circle cx="7" cy="7" r="6" fill="none" stroke="#fff" stroke-width="1.6"/><path d="M5.5 4 8.5 7 5.5 10" fill="none" stroke="#fff" stroke-width="1.6"/></svg>Send Message</div>
</aside>

<div class="abs svc-rule"></div>
<section>
  <div class="abs svc-photo" role="img" aria-label="Photo of a man resting beside stacked moving boxes labelled by room, framed by a white house outline"></div>
  <div class="abs svc-list"></div>
  <div class="abs svc" style="top:1512px">
    <div class="ic"><svg width="26" height="24" viewBox="0 0 26 24"><path d="M13 2 1 13h4v10h16V13h4z" fill="#222"/><rect x="10" y="15" width="6" height="8" fill="#fff"/></svg></div>
    <h4>Residential / Local</h4><p>Lorem Ipsum is simply dummy text of the printing and typesetting industry.</p></div>
  <div class="abs svc" style="top:1605px">
    <div class="ic"><svg width="26" height="24" viewBox="0 0 26 24" fill="none" stroke="#222" stroke-width="2"><path d="M3 9 13 3l10 6v12H3z"/><path d="M3 9l10 6 10-6M13 15v6"/></svg></div>
    <h4>Box Delivery</h4><p>Lorem Ipsum is simply dummy text of the printing and typesetting industry.</p></div>
  <div class="abs svc" style="top:1702px">
    <div class="ic"><svg width="28" height="22" viewBox="0 0 28 22"><rect x="1" y="3" width="17" height="13" fill="#222"/><path d="M18 7h5l4 5v4h-9z" fill="#222"/><circle cx="6" cy="18" r="3" fill="#222"/><circle cx="22" cy="18" r="3" fill="#222"/></svg></div>
    <h4>Commercial/Office</h4><p>Lorem Ipsum is simply dummy text of the printing and typesetting industry.</p></div>
  <div class="abs svc" style="top:1802px">
    <div class="ic"><svg width="22" height="28" viewBox="0 0 22 28" fill="none" stroke="#222" stroke-width="2"><path d="M4 2v20h14"/><rect x="8" y="8" width="9" height="10"/><circle cx="6" cy="24" r="3"/></svg></div>
    <h4>Loading/Unloading</h4><p>Lorem Ipsum is simply dummy text of the printing and typesetting industry.</p></div>
  <div class="abs svc" style="top:1900px;border:none">
    <div class="ic"><svg width="24" height="28" viewBox="0 0 24 28" fill="#222"><circle cx="7" cy="4" r="3"/><rect x="4" y="8" width="6" height="12"/><rect x="12" y="12" width="10" height="10"/><circle cx="15" cy="25" r="2"/></svg></div>
    <h4>Domestic Removals</h4><p>Lorem Ipsum is simply dummy text of the printing and typesetting industry.</p></div>
</section>

<section class="abs plan">
  <h2>Plan your moving &amp; save $100</h2>
  <p>Lorem Ipsum is simply dummy text of the printing and typesetting industry. Lorem Ipsum has been the industry's standard dummy text ever since the 1500s, when an unknown printer took...</p>
  <div class="abs plan-btn"><svg width="12" height="12" viewBox="0 0 14 14"><circle cx="7" cy="7" r="6" fill="none" stroke="#fff" stroke-width="1.6"/><path d="M5.5 4 8.5 7 5.5 10" fill="none" stroke="#fff" stroke-width="1.6"/></svg>Plan Moving</div>
</section>

<section class="testi">
  <h2 class="section-title">TESTIMONIALS</h2>
  <div class="section-title sub">Our customers are saying about our company</div>
  <div class="abs divider" style="left:401px;top:2309px;width:400px"></div>

  <article class="abs card" style="left:160px">
    <div class="avatar"><div role="img" aria-label="Portrait photo of Mara Velden" style="background:radial-gradient(circle at 50% 40%,#e8d3c4,#b98a6e 60%,#6b4636)"></div></div>
    <h5>MARA VELDEN</h5>
    <div class="role">CLIENT OF &nbsp;KESSEL - DALTON</div>
    <p>Lorem Ipsum is simply dummy text of the printing and typesetting industry. Lorem Ipsum has been the industry's standard dummy text ever since the 1500s...</p>
    <div class="rating">★ ★ ★ ★<span>4.0 star Rating</span></div>
  </article>
  <article class="abs card" style="left:609px">
    <div class="avatar"><div role="img" aria-label="Portrait photo of Teo Brannick" style="background:radial-gradient(circle at 50% 40%,#d9c2b0,#8d7565 55%,#3d3a3a)"></div></div>
    <h5>TEO BRANNICK</h5>
    <div class="role">CLIENT OF &nbsp;KESSEL - DALTON</div>
    <p>Lorem Ipsum is simply dummy text of the printing and typesetting industry. Lorem Ipsum has been the industry's standard dummy text ever since the 1500s...</p>
    <div class="rating">★ ★ ★ ★<span>4.0 star Rating</span></div>
  </article>

  <i class="abs pager" style="left:573px"></i>
  <i class="abs pager" style="left:594px;background:var(--blue);outline:2px solid #cfe9f7"></i>
  <i class="abs pager" style="left:615px"></i>
</section>

<footer class="abs footer">
  <div class="dots"><i></i><i></i><i></i></div>
  <small>ALL RIGHT RESERVED 2017.</small>
</footer>

</body>
</html>
```